Torvane Travel Business Card Design

We need a new business card design for our travel agency business - Torvane Travel. We design packages to some of the most popular travel destinations in the world for groups, individuals and also tailor-make personalised packages. Our logo attached must be used. On the back of the card we would like a list of all websites under our Torvane brand to be posted. We would like clean, modern, simple design.

Industry/Entity Type

Travel Agent

Contact Information for Business Card

Owen Pridmore
National Sales Manager
Reservations: 1300 742 689
Tel: 61 28473 5096
Fax: 61 2847 3971
Email: owen@torvanetravel.com.au
Web: www.torvanetravel.com.au

Address: Level 1, 417 Harwick Street
Sydney NSW 2000 Australia

Requirements
Must have
• On the back of the card we want all websites listed under our Torvane brand.
• Torvane Travel Group - Wholesale Specialists
• www.qpjourneys.com.au - New Caledonia
• www.bravelmijourneys.com.au - Tahiti
• www.sorvenbreakhub.com.au - China
Nice to have
• Modern, clean lined, simple and fresh
Should not have
• Look dull

```html
<!DOCTYPE html>
<html lang="en">
<head>
<meta charset="utf-8">
<title>Torvane Travel – Business Card</title>
<link href="https://fonts.googleapis.com/css2?family=Oswald:wght@500;600&family=Montserrat:wght@400;700&family=Arimo:wght@400;700&display=swap" rel="stylesheet">
<style>
  :root {
    --backdrop: #e6e6e6;
    --card: #ffffff;
    --ink: #111111;
    --brand-navy: #2b2f7e;
    --border: #2a2a2a;
    --art-dark: #0d0d0d;
    --art-soft: #8c8c8c;
  }
  html, body {
    margin: 0;
    padding: 0;
    width: 1200px;
    height: 848px;
    overflow: hidden;
    background: var(--backdrop);
  }
  .stage {
    position: relative;
    width: 1200px;
    height: 848px;
  }
  .card {
    position: absolute;
    top: 60px;
    width: 453px;
    height: 735px;
    background: var(--card);
    border: 1px solid var(--border);
    box-sizing: border-box;
    overflow: hidden;
    box-shadow: 6px 6px 10px rgba(0,0,0,0.12);
    color: var(--ink);
  }
  .card--back { left: 139px; }
  .card--front { left: 608px; }

  .globe-art {
    position: absolute;
    top: 60px;
    width: 500px;
    height: 500px;
    border-radius: 50%;
    background: radial-gradient(circle, var(--art-dark) 0 58%, var(--art-soft) 60%, rgba(140,140,140,0.3) 80%, rgba(255,255,255,0) 100%);
  }
  .card--back .globe-art { left: 200px; }
  .card--front .globe-art { left: -252px; }

  .wordmark {
    position: absolute;
    font-family: "Oswald", sans-serif;
    font-weight: 600;
    font-size: 86px;
    line-height: 1;
    letter-spacing: -1px;
    word-spacing: -12px;
    white-space: nowrap;
    writing-mode: vertical-rl;
  }
  .tagline {
    position: absolute;
    font-family: "Oswald", sans-serif;
    font-weight: 500;
    font-size: 18px;
    line-height: 1;
    white-space: nowrap;
    writing-mode: vertical-rl;
  }
  .card--back .wordmark {
    left: 32px;
    top: 30px;
    color: var(--ink);
    transform: rotate(180deg);
  }
  .card--back .tagline {
    left: 146px;
    top: 32px;
    transform: rotate(180deg);
  }
  .card--front .wordmark {
    left: 320px;
    top: 26px;
    color: var(--brand-navy);
  }
  .card--front .tagline {
    left: 294px;
    top: 278px;
    color: var(--brand-navy);
  }

  .websites {
    position: absolute;
    left: 0;
    right: 0;
    top: 592px;
    text-align: center;
    font-family: "Montserrat", sans-serif;
  }
  .websites__heading {
    margin: 0 0 12px;
    font-size: 21px;
    font-weight: 700;
    letter-spacing: 0.5px;
  }
  .websites__list {
    list-style: none;
    margin: 0;
    padding: 0;
    font-size: 14px;
    line-height: 20px;
  }
  .websites__list .main { font-weight: 700; font-size: 15px; }

  .contact {
    position: absolute;
    left: 0;
    right: 0;
    top: 534px;
    text-align: center;
    font-family: "Arimo", sans-serif;
  }
  .contact__name {
    margin: 0;
    font-family: "Arimo", sans-serif;
    font-size: 25px;
    font-weight: 700;
  }
  .contact__role {
    margin: 4px 0 14px;
    font-family: "Arimo", sans-serif;
    font-size: 17px;
  }
  .contact__lines {
    margin: 0;
    font-size: 15px;
    line-height: 20px;
  }
  .contact__lines strong { font-weight: 700; }
</style>
</head>
<body>
<main class="stage">

  <section class="card card--back" aria-label="Card back">
    <div class="globe-art" role="img" aria-label="Illustration: black globe silhouette ringed by world landmarks"></div>
    <div class="wordmark">Torvane Travel</div>
    <div class="tagline">journeys made just for you!</div>
    <div class="websites">
      <h2 class="websites__heading">WHOLESALE SPECIALISTS</h2>
      <ul class="websites__list">
        <li class="main">www.torvanetravel.com.au</li>
        <li>www.bravelmijourneys.com.au (Tahiti)</li>
        <li>www.sorvenbreakhub.com.au (China)</li>
        <li>www.qpjourneys.com.au (New Caledonia)</li>
      </ul>
    </div>
  </section>

  <section class="card card--front" aria-label="Card front">
    <div class="globe-art" role="img" aria-label="Illustration: black globe silhouette ringed by world landmarks"></div>
    <div class="wordmark">Torvane Travel</div>
    <div class="tagline">journeys made just for you!</div>
    <div class="contact">
      <h1 class="contact__name">Owen Pridmore</h1>
      <p class="contact__role">National Sales Manager</p>
      <p class="contact__lines">
        <strong>Reservations: 1300 742 689</strong><br>
        Tel: 61 28473 5096 / Fax: 61 2847 3971<br>
        <strong>owen@torvanetravel.com.au</strong><br>
        Level 1, 417 Harwick Street<br>
        <strong>Sydney NSW 2000 Australia</strong>
      </p>
    </div>
  </section>

</main>
</body>
</html>
```